Bright Harbor Galas one stop event solution

A new event company base in Singapore.
Specialist in PARTIES & SPECIAL EVENTS
FULL EVENT ORGANIZERS

Bright Harbor Galas provide all events need ranging from small to large number of people who are looking for a different way of organizing their event. We have a team of talented experience people working in a team to make your event more memorable moments...
Updates

Project Deadline Extended Reason: Date line is to rush would like to give them more time and more time for me to think Added Sunday, August 2, 2015

Target Market(s)

Club
Embassy
Pubs
Organisation
Community Events
ETC

Industry/Entity Type

Entertainment Industry

Font styles to use
Script

Colors
000000
fec214

Requirements
Must have
• anything that related to entertainment and event...
Nice to have
• Must be in gold and black color for the theme... wording and graphic in gold while the base background will be black...
Should not have
• Non

```html
<!DOCTYPE html>
<html lang="en">
<head>
<meta charset="utf-8">
<title>Bright Harbor Galas — One Stop Event Solution</title>
<link href="https://fonts.googleapis.com/css2?family=Arvo:wght@700&family=Lobster+Two:ital,wght@0,400;1,400&family=Open+Sans:wght@400;600&display=swap" rel="stylesheet">
<style>
:root{
  --gold:#fec214;
  --gold-deep:#d9a514;
  --black:#000000;
  --ink:#1b1b1b;
  --nav:#2a2a2a;
  --text:#555555;
  --muted:#8a8a8a;
  --paper:#ffffff;
  --sand:#f3ecdc;
  --line:#e2e2e2;
}
*{margin:0;padding:0;box-sizing:border-box}
html,body{width:1200px;height:2196px;overflow:hidden}
body{position:relative;background:var(--paper);font-family:"Open Sans",Arial,sans-serif;color:var(--text)}
.abs{position:absolute}

/* header */
.topbar{left:0;top:0;width:1200px;height:72px;background:rgba(20,20,20,.85);z-index:3}
.brand{left:48px;top:0;width:184px;height:170px;background:var(--gold);z-index:4;display:flex;align-items:center;justify-content:center;gap:10px;padding:0 14px}
.brand-dot{width:18px;height:18px;border-radius:50%;background:var(--paper);flex:none}
.brand-name{font-family:"Open Sans",Arial,sans-serif;font-weight:600;font-size:22px;line-height:1.2;color:var(--paper)}
.search{left:252px;top:18px;width:300px;height:36px;display:flex;align-items:center;gap:12px;color:#9a9a9a;font-size:17px}
.nav{left:588px;top:0;height:72px;display:flex;z-index:4}
.nav a{display:flex;align-items:center;padding:0 20px;height:72px;color:#e8e8e8;font-size:17px;text-decoration:none}
.nav a.active{background:var(--gold);color:var(--paper)}
.nav .caret{margin-left:6px;font-size:11px}

/* hero */
.hero{left:0;top:0;width:1200px;height:740px;
  background:
   radial-gradient(circle at 78% 18%,rgba(190,200,255,.85) 0,rgba(120,90,200,.35) 14%,transparent 30%),
   radial-gradient(circle at 40% 8%,rgba(230,80,160,.55) 0,transparent 22%),
   radial-gradient(ellipse at 70% 70%,rgba(110,60,140,.6) 0,transparent 45%),
   linear-gradient(180deg,#2a1d3c 0%,#3a2140 45%,#1a1420 100%)}
.hero-title{left:64px;top:228px;width:760px;font-family:"Arvo",Georgia,serif;font-weight:700;font-size:50px;line-height:1.3;color:var(--paper)}
.hero-text{left:64px;top:420px;width:640px;font-size:19px;line-height:1.55;color:#e6e6e6}
.btn{height:42px;width:140px;display:flex;align-items:center;justify-content:center;font-size:16px;color:var(--paper)}
.btn-outline{left:64px;top:568px;border:2px solid var(--gold)}
.btn-gold{left:224px;top:568px;background:var(--gold)}
.dots{display:flex;gap:10px}
.dot{width:16px;height:16px;border-radius:50%;border:2px solid var(--paper)}
.dot.on{background:var(--paper)}
.hero-dots{left:568px;top:662px}

/* about */
.section-title{font-family:"Lobster Two",Georgia,cursive;font-size:46px;color:var(--gold-deep);text-align:center}
.about-title{left:0;top:776px;width:1200px}
.rule{left:560px;top:846px;width:80px;height:3px;background:var(--gold)}
.about-text{left:250px;top:868px;width:700px;text-align:center;font-size:15px;line-height:1.75;color:var(--muted)}

/* cards */
.card{top:1016px;width:326px;height:470px}
.card-tab{position:absolute;left:0;top:0;width:110px;height:40px;background:#eeeeee;border-radius:10px 10px 0 0;display:flex;align-items:center;justify-content:center;font-size:15px;color:#444}
.card-media{position:absolute;left:0;top:40px;width:326px;height:168px}
.card-band{position:absolute;left:0;top:118px;width:326px;height:44px;background:rgba(254,194,20,.85);display:flex;align-items:center;justify-content:center;font-family:"Lobster Two",Georgia,cursive;font-style:italic;font-size:26px;color:var(--paper)}
.card-title{position:absolute;left:0;top:226px;width:326px;font-size:18px;line-height:1.35;color:var(--gold-deep)}
.card-text{position:absolute;left:0;top:286px;width:326px;font-size:14px;line-height:1.7;color:var(--muted)}
.card-more{position:absolute;left:0;top:412px;font-size:15px;color:#333}
.media-latest{background:linear-gradient(135deg,#7a2a1c,#c86a2a 45%,#3a1410)}
.media-events{background:radial-gradient(circle at 50% 20%,#9bb6ff,transparent 40%),linear-gradient(180deg,#1f2f7a,#0e1434)}
.media-services{background:linear-gradient(135deg,#d9b98a,#f1e2c4 50%,#a88460)}

/* testimonial */
.quote-band{left:0;top:1508px;width:1200px;height:280px;background:radial-gradient(ellipse at 70% 30%,#3b4b6e,transparent 60%),linear-gradient(180deg,#1c2233,#0d0f17)}
.avatar{left:40px;top:1540px;width:164px;height:164px;border-radius:50%;border:5px solid var(--paper);background:linear-gradient(160deg,#c9b69a,#6f5b48)}
.quote-name{left:236px;top:1566px;font-family:"Lobster Two",Georgia,cursive;font-size:40px;color:var(--paper)}
.quote-text{left:236px;top:1632px;width:900px;font-size:16px;line-height:1.65;color:#e1e1e1}
.quote-text::before{content:"\201C";font-size:30px;color:var(--gold);margin-right:8px;vertical-align:-6px}
.quote-dots{left:560px;top:1746px}

/* footer */
.footer{left:0;top:1808px;width:1200px;height:336px;background:var(--sand)}
.foot-head{font-family:"Lobster Two",Georgia,cursive;font-size:34px;color:var(--gold-deep)}
.foot-rule{width:560px;height:1px;background:#d8ceb6}
.foot-text{font-size:14px;line-height:1.75;color:#7a7a7a}
.social{left:56px;top:2014px;display:flex;gap:14px}
.social span{width:52px;height:52px;border-radius:50%;background:var(--gold)}
.subscribe{left:620px;top:2030px;width:520px;height:54px;display:flex}
.subscribe .field{flex:1;background:var(--paper);display:flex;align-items:center;padding:0 22px;font-size:15px;color:#888}
.subscribe .go{width:150px;background:var(--gold);color:var(--paper);display:flex;align-items:center;justify-content:center;font-size:16px}
.bottom{left:0;top:2144px;width:1200px;height:52px;background:var(--ink);display:flex;align-items:center;padding-left:56px;font-size:14px;color:#aaa}
</style>
</head>
<body>

<div class="abs hero" role="img" aria-label="Concert crowd under bright stage lights"></div>

<header>
  <div class="abs topbar"></div>
  <div class="abs brand"><span class="brand-dot"></span><span class="brand-name">Bright Harbor Galas</span></div>
  <div class="abs search">
    <svg width="20" height="20" viewBox="0 0 20 20" fill="none" stroke="#bbb" stroke-width="2.4"><circle cx="8" cy="8" r="6"/><path d="M12.5 12.5 18 18"/></svg>
    Search
  </div>
  <nav class="abs nav">
    <a class="active">Home</a>
    <a>About<span class="caret">▼</span></a>
    <a>Services</a>
    <a>News</a>
    <a>Gallery<span class="caret">▼</span></a>
    <a>Hall</a>
  </nav>
</header>

<section>
  <h1 class="abs hero-title">Donec ut turpis sit amet enim mattis commodo velit.</h1>
  <p class="abs hero-text">We provide events from a small crowd to grand galas, organised to match each guest need with care.</p>
  <div class="abs btn btn-outline">Contact</div>
  <div class="abs btn btn-gold">Read More</div>
  <div class="abs dots hero-dots"><span class="dot"></span><span class="dot on"></span><span class="dot"></span></div>
</section>

<section>
  <h2 class="abs section-title about-title">About Us</h2>
  <div class="abs rule"></div>
  <p class="abs about-text">Lorem ipsum dolor sit amet, consectetur adipiscing elit. Integer vel nisi enim, sed lobortis pellentesque. Sed rhoncus, eros nec euismod ultrices lectus nulla varius massa, at blandit nunc ex vel felis pellentesque imperdiet nisi.</p>

  <article class="abs card" style="left:64px">
    <div class="card-tab">Latest</div>
    <div class="card-media media-latest" role="img" aria-label="Banquet hall set for a gala dinner"><div class="card-band">Latest</div></div>
    <h3 class="card-title">Morbi pellentesque urna scelerisque justo rutrum</h3>
    <p class="card-text">Lorem ipsum dolor sit amet, consectetur adipiscing elit. Nulla mattis magna in hendrerit. Pellentesque non nisl, sagittis eget elit non augue.</p>
    <div class="card-more">» Read More</div>
  </article>

  <article class="abs card" style="left:437px">
    <div class="card-tab">Events</div>
    <div class="card-media media-events" role="img" aria-label="Stage with blue lights and an audience"><div class="card-band">Events</div></div>
    <h3 class="card-title">Morbi pellentesque urna scelerisque justo rutrum</h3>
    <p class="card-text">Lorem ipsum dolor sit amet, consectetur adipiscing elit. Nulla mattis magna in hendrerit. Pellentesque non nisl, sagittis eget elit non augue.</p>
    <div class="card-more">» Read More</div>
  </article>

  <article class="abs card" style="left:806px">
    <div class="card-tab">Services</div>
    <div class="card-media media-services" role="img" aria-label="Decorated reception tables with flowers"><div class="card-band">Services</div></div>
    <h3 class="card-title">Morbi pellentesque urna scelerisque justo rutrum</h3>
    <p class="card-text">Lorem ipsum dolor sit amet, consectetur adipiscing elit. Nulla mattis magna in hendrerit. Pellentesque non nisl, sagittis eget elit non augue.</p>
    <div class="card-more">» Read More</div>
  </article>
</section>

<section>
  <div class="abs quote-band" role="img" aria-label="Audience with raised hands at a concert"></div>
  <div class="abs avatar" role="img" aria-label="Portrait of the client giving the testimonial"></div>
  <div class="abs quote-name">Clara Hendon</div>
  <p class="abs quote-text">Lorem ipsum dolor sit amet consectetur adipiscing elit, sed do eiusmod tempor incididunt ut labore et dolore magna aliqua. Ut enim ad minim veniam, quis nostrud exercitation ullamco laboris nisi ut aliquip commodo.</p>
  <div class="abs dots quote-dots"><span class="dot"></span><span class="dot on"></span><span class="dot"></span></div>
</section>

<footer>
  <div class="abs footer"></div>
  <h4 class="abs foot-head" style="left:56px;top:1836px">About</h4>
  <div class="abs foot-rule" style="left:56px;top:1890px;width:500px"></div>
  <p class="abs foot-text" style="left:56px;top:1904px;width:500px">Nam at interdum dui, eget mattis augue. Cras sagittis orci urna, quis cursus diam sollicitudin id. Nullam in convallis diam. Aliquam tincidunt pharetra, sed ut semper elit, magna feugiat nisl commodo fermentum venenatis.</p>
  <div class="abs social"><span></span><span></span><span></span><span></span></div>

  <h4 class="abs foot-head" style="left:620px;top:1836px">Newsletter</h4>
  <div class="abs foot-rule" style="left:620px;top:1890px;width:520px"></div>
  <p class="abs foot-text" style="left:620px;top:1904px;width:520px">Aenean sagittis erat eget elit quam sit amet, consectetur adipiscing elit. Phasellus non purus et consectetur vulputate.</p>
  <div class="abs subscribe"><div class="field">Enter Email</div><div class="go">Subscribe</div></div>

  <div class="abs bottom">© 2015 Bright Harbor Galas. All rights reserved.</div>
</footer>

</body>
</html>
```